Create 6 animated banners for makerting promotion

Create 6 animated banners similar to the example provided

Banner size needed

1 x 300x250
1 x 160x600
1 x 468x60
1 x 728x90
1 x 120x600
1 x 200x200

Text to be displayed:

intro screen: Pixelgrove.com
animation > screen 1: The Most Refined Ad Serving Platform (pause 1.5 seconds)
animation > screen 2: Publishers - Get The Highest CPM Rates! (pause 1.5 seconds)
animation > screen 3: Advertisers - Get The Highest ROI! (pause 1.5 seconds)
animation > screen 4: Simple Dashboard (pause 1.5 seconds)
animation > screen 5: Profit From Top Quality Traffic (pause 1.5 seconds)
animation > screen 6: Account Managers Available To Help You Succeed (pause 1.5 seconds)
animation > screen 7: Click Here To Register (pause 1.5 seconds)
animation > screen 8: Pixelgrove.com (pause 1.5 seconds)

background color: #0795d3

image provided must be animated gif

Attracted file with logo and sample banner
pixelgrove.com logo font is Blender Pro Heavy

Target Market(s)

professional marketers, advertisers and publishers

Industry/Entity Type

Advertising

Font styles to use
Sans Serif

Requirements
Must have
• requirement text provided on description
• image must be animated gif
Nice to have
• slick animation
Should not have
• end image size should not be over 500kb

```html
<!DOCTYPE html>
<html lang="en">
<head>
<meta charset="UTF-8">
<title>Pixelgrove.com – Skyscraper Banner Frames</title>
<link rel="stylesheet" href="https://fonts.googleapis.com/css2?family=Roboto:wght@500&family=Barlow+Semi+Condensed:wght@800&display=swap">
<style>
  :root {
    --brand-blue: #0795d3;
    --brand-blue-deep: #078bc7;
    --paper: #ffffff;
    --ink-light: #ffffff;
  }
  * { margin: 0; padding: 0; box-sizing: border-box; }
  html, body {
    width: 1200px;
    height: 900px;
    overflow: hidden;
    background: var(--paper);
    font-family: "Roboto", "Helvetica Neue", Arial, sans-serif;
    font-weight: 500;
  }
  .storyboard {
    position: relative;
    width: 1200px;
    height: 900px;
  }
  .banner-frame {
    position: absolute;
    top: 150px;
    width: 160px;
    height: 600px;
    background: var(--brand-blue);
    color: var(--ink-light);
    text-align: center;
  }
  .banner-frame:nth-child(1) { left: 58px; }
  .banner-frame:nth-child(2) { left: 242px; }
  .banner-frame:nth-child(3) { left: 427px; }
  .banner-frame:nth-child(4) { left: 612px; }
  .banner-frame:nth-child(5) { left: 797px; }
  .banner-frame:nth-child(6) { left: 982px; }

  .brand-mark-faint {
    position: absolute;
    left: 18px;
    top: 238px;
    width: 124px;
    height: 124px;
    background: var(--brand-blue-deep);
  }
  .headline {
    position: absolute;
    left: 0;
    right: 0;
    font-size: 18.5px;
    letter-spacing: -0.3px;
    white-space: nowrap;
  }
  .headline p { line-height: 25px; }
  .headline.tall p { line-height: 28px; }
  .tag-label {
    display: inline-block;
    background: var(--paper);
    color: var(--brand-blue);
    font-size: 18.5px;
    line-height: 28px;
    padding: 0 6px;
    margin-bottom: 14px;
    letter-spacing: 0;
  }
  .headline-plain { top: 56px; }
  .headline-publishers { top: 68px; }
  .headline-advertisers { top: 72px; }
  .headline-dashboard { top: 86px; }
  .headline-managers { top: 37px; }
  .headline-managers .gap { margin-top: 5px; }
  .headline-managers .tag-label { margin-top: 15px; margin-bottom: 0; }

  .call-to-action {
    position: absolute;
    left: 0;
    right: 0;
    top: 437px;
    font-size: 22.5px;
    line-height: 28px;
    letter-spacing: -0.4px;
  }
  .site-label {
    position: absolute;
    left: 6px;
    top: 560px;
    width: 148px;
    height: 27px;
    background: var(--paper);
    color: var(--brand-blue);
    font-family: "Barlow Semi Condensed", "Arial Narrow", sans-serif;
    font-weight: 800;
    font-size: 19px;
    line-height: 27px;
    text-transform: uppercase;
    letter-spacing: 0;
  }
</style>
</head>
<body>
<main class="storyboard">
  <section class="banner-frame intro">
    <div class="brand-mark-faint"></div>
  </section>

  <section class="banner-frame">
    <div class="brand-mark-faint"></div>
    <div class="headline headline-plain">
      <p>The Most<br>Refined<br>Ad Serving<br>Platform</p>
    </div>
    <div class="call-to-action">Click Here<br>To Register</div>
    <div class="site-label">pixelgrove.com</div>
  </section>

  <section class="banner-frame">
    <div class="brand-mark-faint"></div>
    <div class="headline headline-publishers tall">
      <span class="tag-label">PUBLISHERS</span>
      <p>Get The Highest<br>CPM Rates!</p>
    </div>
    <div class="call-to-action">Click Here<br>To Register</div>
    <div class="site-label">pixelgrove.com</div>
  </section>

  <section class="banner-frame">
    <div class="brand-mark-faint"></div>
    <div class="headline headline-advertisers tall">
      <span class="tag-label">ADVERTISERS</span>
      <p>Get The Highest<br>ROI!</p>
    </div>
    <div class="call-to-action">Click Here<br>To Register</div>
    <div class="site-label">pixelgrove.com</div>
  </section>

  <section class="banner-frame">
    <div class="brand-mark-faint"></div>
    <div class="headline headline-dashboard tall">
      <p>Simple<br>Dashboard</p>
    </div>
    <div class="call-to-action">Click Here<br>To Register</div>
    <div class="site-label">pixelgrove.com</div>
  </section>

  <section class="banner-frame">
    <div class="brand-mark-faint"></div>
    <div class="headline headline-managers">
      <p>Account<br>Managers</p>
      <p class="gap">Available<br>To Help You</p>
      <span class="tag-label">SUCCEED</span>
    </div>
    <div class="call-to-action">Click Here<br>To Register</div>
    <div class="site-label">pixelgrove.com</div>
  </section>
</main>
</body>
</html>
```